BrivoMatex. Lantern for the Steady Growth. Business card

Professional business card for BrivoMatex (Lantern for the Steady Growth)
My rationale: Strategy-> Execution-> Results-> Value that lead to the BrivoMatex name: We put the Lantern for the Steady Growth.
We deliver value to our customers helping them at defining a good strategy (cyan arrow). 90% of well formulated strategies fail due to poor execution so we also consider strategical execution very important (green arrow). Due to the execution we obtain the results (blue arrow). Finally, the results provide feedback to redefine strategy, and the new strategy has to be executed and new results obtained providing new feedback and on and on. It's like a wheel that finally, must create corporate value: value for shareholders, staholders, employees, providers...-

Target Market(s)

CEOs and steering comitees , invewrnent funds

Industry/Entity Type

Business Consultant

Contact Information for Business Card

Tommaso Ferlini
CEO & Founder
tommaso.ferlini@brivomatex.example
Mobile: +34 611.205.938
www.brivomatex.example

Colors

Designer to choose colors to be used in the design.

Requirements
Nice to have
• Nice to hace the words: Strategy, execution, results
• Nice to vave the claim: Lantern for the Steady Growth
• The three colors should be shown:
• cyan for STRATEGY
• green for EXECUTION
• blue for RESULTS
Should not have
• Complete black background

```html
<!DOCTYPE html>
<html lang="en">
<head>
<meta charset="utf-8">
<title>BrivoMatex Business Card</title>
<link href="https://fonts.googleapis.com/css2?family=Lato:wght@400;700;900&display=swap" rel="stylesheet">
<style>
  :root {
    --backdrop: #3b3c3f;
    --brand-blue: #253f94;
    --brand-navy: #1f3385;
    --brand-cyan: #2cb3e6;
    --brand-green: #8dc63f;
    --card-white: #ffffff;
    --text-grey: #4a4a4a;
  }
  * { margin: 0; padding: 0; box-sizing: border-box; }
  html, body {
    width: 1200px; height: 900px; overflow: hidden;
    background: var(--backdrop);
    font-family: "Lato", sans-serif;
  }
  .canvas {
    position: relative; width: 1200px; height: 900px;
  }
  .card {
    position: absolute; left: 290px;
    width: 620px; height: 360px;
    border-radius: 18px;
    box-shadow: 0 10px 24px rgba(0,0,0,0.35);
    overflow: hidden;
  }
  /* Back side */
  .card-back {
    top: 50px;
    background: var(--brand-blue);
    color: var(--card-white);
  }
  .card-back .brand-name {
    position: absolute; left: 0; right: 0; top: 140px;
    text-align: center;
    font-weight: 900; font-size: 60px; letter-spacing: -1px;
    color: var(--card-white);
  }
  .card-back .brand-mark {
    position: absolute; left: 294px; top: 100px;
    width: 32px; height: 32px; border-radius: 50%;
    background: var(--card-white);
  }
  .card-back .brand-url {
    position: absolute; left: 0; right: 0; top: 292px;
    text-align: center;
    font-size: 14px; letter-spacing: 5px;
  }
  /* Front side */
  .card-front {
    top: 490px;
    background: var(--card-white);
  }
  .card-front .brand-block {
    position: absolute; left: 0; top: 0; width: 310px; height: 360px;
  }
  .card-front .brand-mark {
    position: absolute; left: 141px; top: 118px;
    width: 28px; height: 28px; border-radius: 50%;
    background: var(--brand-navy);
  }
  .card-front .brand-name {
    position: absolute; left: 0; right: 0; top: 158px;
    text-align: center;
    font-weight: 900; font-size: 46px; letter-spacing: -1px;
    color: var(--brand-navy);
  }
  .card-front .divider {
    position: absolute; left: 310px; top: 120px;
    width: 1.5px; height: 150px;
    background: var(--brand-navy);
  }
  .contact-block {
    position: absolute; left: 332px; top: 82px; right: 16px;
    color: var(--text-grey);
  }
  .person-name {
    font-weight: 900; font-size: 25px; color: var(--brand-navy);
    line-height: 1.1;
  }
  .person-role {
    font-size: 14px; margin-top: 4px;
  }
  .address {
    font-size: 13px; line-height: 1.35; margin-top: 12px;
  }
  .contact-list {
    list-style: none; margin-top: 12px;
  }
  .contact-list li {
    display: flex; align-items: center;
    font-size: 13px; line-height: 1.6;
  }
  .contact-list svg {
    width: 13px; height: 13px; margin-right: 8px; flex: none;
  }
</style>
</head>
<body>
<div class="canvas">

  <section class="card card-back" aria-label="Business card, back">
    <span class="brand-mark"></span>
    <div class="brand-name">BrivoMatex</div>
    <div class="brand-url">www.brivomatex.example</div>
  </section>

  <section class="card card-front" aria-label="Business card, front">
    <div class="brand-block">
      <span class="brand-mark"></span>
      <div class="brand-name">BrivoMatex</div>
    </div>
    <div class="divider"></div>
    <div class="contact-block">
      <div class="person-name">Tommaso Ferlini</div>
      <div class="person-role">Founder &amp; CEO</div>
      <div class="address">Avda. Marítima 214,<br>Valencia, 46011 España</div>
      <ul class="contact-list">
        <li>
          <svg viewBox="0 0 16 16" aria-hidden="true"><path d="M4 1.5 6.2 4 5 5.6c.8 1.8 2.2 3.2 4 4l1.6-1.2 2.5 2.2-1.3 2.4C7 12.6 3.4 9 2.5 3z" fill="var(--brand-cyan)"/></svg>
          +34 611.205.938
        </li>
        <li>
          <svg viewBox="0 0 16 16" aria-hidden="true"><rect x="1" y="3" width="14" height="10" rx="1" fill="var(--brand-cyan)"/><path d="M1.5 3.5 8 9l6.5-5.5" stroke="#fff" stroke-width="1.2" fill="none"/></svg>
          tommaso.ferlini@brivomatex.example
        </li>
        <li>
          <svg viewBox="0 0 16 16" aria-hidden="true"><circle cx="8" cy="8" r="7" fill="var(--brand-cyan)"/><path d="M1 8h14M8 1v14M3 4.5h10M3 11.5h10" stroke="#fff" stroke-width=".9" fill="none"/><ellipse cx="8" cy="8" rx="3.2" ry="7" stroke="#fff" stroke-width=".9" fill="none"/></svg>
          www.brivomatex.example
        </li>
      </ul>
    </div>
  </section>

</div>
</body>
</html>
```